Up to the Challenge? Canadian based consulting company needs a two sided business card design

A Canadian based security risk management consulting company needs a two-sided business card design. What we do is provide advice and guidance related to emergency, security and business continuity management for small, medium and large companies to help ensure the protection of their people, assets, information, services, operations and reputation.

The final design should be simple, only one or two colours, eye catching, professional and one that makes people look at three or more times just because it looks so darn good.

I have include examples of business cards I like.

Target Market(s)

Small, medium and large companies.

Industry/Entity Type

Security

Contact Information for Business Card

Business Card Size: Standard size of 3.5" (89mm) x 2.0" (51mm) - (see full specifications and guides on PRINTA's website if required)
Card Stock: Looking to use PRINTA's Velda 32pt stock textured paper - seam colour either chili red or black
Business Name: The Harrowfield Group
Website: www.theharrowfieldgroup.example
Telephone: (555)214-0397
Name: Dana Forsythe
Position: Principle
e-mail: Dana.Forsythe@theharrowfieldgroup.example

Font styles to use
Serif

Colors
ec1f27
000000
9d9d9d
aaaaaa
606060

Requirements
Must have
• - "The Harrowfield Group" logo (see uploaded files). I have included grey scale and colour versions.
• - Business card details (as above)
Nice to have
• - One side black or grey scale.
• - Other side would likely be white.
• - Everyone likes the silver logo on the black background.
• - Small element of colour i.e. red but I'm leaning more to greyscale.
Should not have
• - A lot of colour. Keep it simple.

```html
<!DOCTYPE html>
<html lang="en">
<head>
<meta charset="utf-8">
<title>The Harrowfield Group — Business Card</title>
<link rel="stylesheet" href="https://fonts.googleapis.com/css2?family=PT+Serif:wght@400;700&display=swap">
<style>
  :root {
    --backdrop: #ebebeb;
    --card-dark: #3a3a3a;
    --card-dark-edge: #2e2e2e;
    --card-light: #ffffff;
    --accent-red: #ec1f27;
    --ink-grey: #606060;
    --soft-grey: #9d9d9d;
    --serif: "PT Serif", Georgia, serif;
  }
  * { box-sizing: border-box; margin: 0; padding: 0; }
  html, body {
    width: 1200px;
    height: 1000px;
    overflow: hidden;
    background: var(--backdrop);
    font-family: var(--serif);
  }
  .canvas {
    position: relative;
    width: 1200px;
    height: 1000px;
  }
  .card {
    position: absolute;
    width: 650px;
    height: 370px;
    box-shadow: 0 3px 8px rgba(0, 0, 0, 0.18);
  }

  /* Front: dark side */
  .card--front {
    left: 280px;
    top: 110px;
    background: linear-gradient(90deg, var(--card-dark-edge), var(--card-dark) 40%, var(--card-dark-edge) 75%, var(--card-dark));
    display: flex;
    flex-direction: column;
    align-items: center;
  }
  .front-brand {
    margin-top: 150px;
    display: flex;
    align-items: center;
    gap: 14px;
    color: var(--accent-red);
    font-size: 30px;
    font-weight: 400;
    letter-spacing: 2px;
    text-transform: uppercase;
  }
  .brand-mark {
    width: 26px;
    height: 26px;
    background: var(--accent-red);
    flex: none;
  }
  .front-web {
    margin-top: auto;
    margin-bottom: 34px;
    color: var(--accent-red);
    font-size: 19px;
  }

  /* Back: white side */
  .card--back {
    left: 255px;
    top: 505px;
    background: var(--card-light);
    display: flex;
    flex-direction: column;
    align-items: center;
    color: var(--ink-grey);
    text-align: center;
  }
  .back-brand {
    margin-top: 42px;
    display: flex;
    align-items: center;
    gap: 12px;
    color: var(--accent-red);
    font-size: 22px;
    letter-spacing: 1.5px;
    text-transform: uppercase;
  }
  .back-brand .brand-mark { width: 22px; height: 22px; }
  .person-name {
    margin-top: 60px;
    font-size: 34px;
    font-weight: 700;
    line-height: 1.05;
  }
  .person-role {
    font-size: 30px;
    line-height: 1.1;
  }
  .contact {
    margin-top: 42px;
    font-size: 22px;
    line-height: 1.3;
  }
</style>
</head>
<body>
  <main class="canvas">
    <section class="card card--front" aria-label="Card front">
      <div class="front-brand">
        <span class="brand-mark" aria-hidden="true"></span>
        <span>The Harrowfield Group</span>
      </div>
      <p class="front-web">www.theharrowfieldgroup.example</p>
    </section>

    <section class="card card--back" aria-label="Card back">
      <div class="back-brand">
        <span class="brand-mark" aria-hidden="true"></span>
        <span>The Harrowfield Group</span>
      </div>
      <h1 class="person-name">Dana Forsythe</h1>
      <p class="person-role">Principle</p>
      <div class="contact">
        <p class="contact-email">Dana.Forsythe@theharrowfieldgroup.example</p>
        <p class="contact-phone">(555)214-0397</p>
      </div>
    </section>
  </main>
</body>
</html>
```